Brazilian food stall looking for a make over

We need a new Design for the front of our stall that would look authentic, colourful and practical as we have to transport, set up and put down in few hours.
We are based in Brisbane and our business are call The Ember Coals.
We sell Brazilian traditional BBQ and vegetarians options at markets, festivals and privet functions. We are new to this business and at the moment we are using our own design as presented on the image below.
We would like to see designs that would be eye catching with high contrast for easy recognition of the product with a menu with images of the product.

Requirements
Must have
• A connection with the product that is Brazilian bbq

```html
<!DOCTYPE html>
<html lang="en">
<head>
<meta charset="utf-8">
<title>The Ember Coals – Stall Front</title>
<link rel="stylesheet" href="https://fonts.googleapis.com/css2?family=Lobster&family=Roboto+Condensed:wght@400;700&display=swap">
<style>
  :root {
    --sun-yellow: #ffe100;
    --card-yellow: #fde200;
    --leaf-green: #1a9c45;
    --ink: #2b2b1a;
    --alert-red: #e0201b;
    --white: #ffffff;
    --ember-dark: #1e0702;
    --ember-mid: #b3300a;
    --ember-hot: #ff9a1c;
    --meat-dark: #2e130a;
    --meat-mid: #8a4020;
    --meat-light: #e0a060;
  }
  * { box-sizing: border-box; margin: 0; padding: 0; }
  html, body { width: 1200px; height: 1080px; overflow: hidden; background: var(--white); }
  .stall-front { position: relative; width: 1200px; height: 1080px; background: var(--white); font-family: "Roboto Condensed", Arial, sans-serif; }

  .banner-title { position: absolute; font-family: "Lobster", cursive; color: var(--sun-yellow); white-space: nowrap; line-height: 1; transform-origin: left center; }
  .brand-mark { position: absolute; display: flex; align-items: center; gap: 12px; }
  .brand-mark .dot { border-radius: 50%; background: var(--sun-yellow); }
  .brand-mark .name { font-family: "Lobster", cursive; color: var(--sun-yellow); line-height: 1; white-space: nowrap; }

  .fire-banner { position: absolute; left: 0; top: 0; width: 1200px; height: 238px;
    background:
      radial-gradient(ellipse at 20% 20%, rgba(255,190,60,.85) 0%, rgba(255,120,20,0) 45%),
      radial-gradient(ellipse at 70% 10%, rgba(255,170,40,.8) 0%, rgba(255,100,10,0) 40%),
      radial-gradient(ellipse at 90% 70%, rgba(230,80,10,.6) 0%, rgba(0,0,0,0) 40%),
      linear-gradient(180deg, var(--ember-hot) 0%, var(--ember-mid) 40%, var(--ember-dark) 100%); }
  .fire-banner .brand-mark { left: 40px; top: 150px; }
  .fire-banner .brand-mark .dot { width: 30px; height: 30px; }
  .fire-banner .brand-mark .name { font-size: 38px; }
  .fire-banner .banner-title { left: 388px; top: 52px; font-size: 114px; transform: rotate(-5deg); }

  .menu-row { position: absolute; left: 0; top: 240px; width: 1200px; height: 245px; }
  .menu-card { position: absolute; top: 0; width: 172px; height: 242px; background: var(--card-yellow); text-align: center; color: var(--ink); }
  .menu-card .card-brand { font-family: "Lobster", cursive; font-size: 19px; color: var(--leaf-green); margin-top: 8px; line-height: 1; }
  .menu-card .dish-name { font-weight: 700; font-size: 13px; line-height: 1.05; margin-top: 2px; }
  .menu-card .dish-photo { position: absolute; left: 20px; top: 64px; width: 132px; height: 100px; }
  .menu-card .price { position: absolute; left: 10px; top: 52px; width: 40px; height: 40px; border-radius: 50%; background: var(--leaf-green);
    color: var(--white); font-weight: 700; font-size: 17px; line-height: 36px; border: 2px solid var(--white); }
  .menu-card .new-flag { position: absolute; right: 4px; top: 146px; width: 32px; height: 32px; border-radius: 50%; background: var(--alert-red);
    color: var(--white); font-size: 11px; font-weight: 700; line-height: 28px; border: 2px solid var(--white); }
  .menu-card .dish-desc { position: absolute; left: 6px; right: 6px; top: 172px; font-size: 9px; line-height: 11.5px; }
  .menu-card .dish-desc.roomy { line-height: 13.5px; top: 174px; }

  .photo-plate { background:
      radial-gradient(ellipse at 30% 62%, #f6f3ec 0%, #f6f3ec 14%, rgba(246,243,236,0) 22%),
      radial-gradient(ellipse at 62% 60%, #2a1a14 0%, #3a2418 18%, rgba(58,36,24,0) 30%),
      radial-gradient(ellipse at 22% 40%, #6f9a3a 0%, rgba(111,154,58,0) 16%),
      radial-gradient(ellipse at 50% 58%, #ffffff 0%, #e9e4da 45%, rgba(233,228,218,0) 62%),
      linear-gradient(180deg, #7a6a58 0%, #3b2c22 100%); }
  .photo-grill { background:
      radial-gradient(ellipse at 55% 75%, #c8584a 0%, #a23a2c 14%, rgba(120,40,25,0) 30%),
      radial-gradient(ellipse at 30% 45%, #6e2c18 0%, #4a1c0e 25%, rgba(74,28,14,0) 45%),
      radial-gradient(ellipse at 80% 30%, #f08a3a 0%, rgba(240,138,58,0) 30%),
      linear-gradient(180deg, #3a160a 0%, #1c0905 100%); }
  .photo-roast { background:
      radial-gradient(ellipse at 25% 40%, #b8642a 0%, #7a3814 20%, rgba(122,56,20,0) 32%),
      radial-gradient(ellipse at 60% 38%, #a85a26 0%, #6e3212 20%, rgba(110,50,18,0) 32%),
      radial-gradient(ellipse at 88% 35%, #9a4e20 0%, rgba(110,50,18,0) 22%),
      linear-gradient(180deg, #2a1408 0%, #0e0603 100%); }
  .photo-veg { background:
      radial-gradient(circle at 14% 28%, #d8281e 0%, #d8281e 9%, rgba(216,40,30,0) 12%),
      radial-gradient(circle at 28% 24%, #d8281e 0%, #d8281e 8%, rgba(216,40,30,0) 11%),
      radial-gradient(ellipse at 68% 28%, #6a8a3a 0%, rgba(106,138,58,0) 12%),
      radial-gradient(ellipse at 86% 28%, #c8442e 0%, rgba(200,68,46,0) 12%),
      radial-gradient(ellipse at 50% 75%, #c88a4a 0%, #e6c89a 30%, rgba(230,200,154,0) 50%),
      linear-gradient(180deg, #fbf9f5 0%, #efe6d6 100%); }
  .photo-picanha { background:
      radial-gradient(circle at 14% 28%, #d8281e 0%, #d8281e 9%, rgba(216,40,30,0) 12%),
      radial-gradient(ellipse at 68% 28%, #6a8a3a 0%, rgba(106,138,58,0) 12%),
      radial-gradient(ellipse at 86% 28%, #c8442e 0%, rgba(200,68,46,0) 12%),
      radial-gradient(ellipse at 55% 75%, #5a2a14 0%, #7a3a1c 22%, #e6c89a 42%, rgba(230,200,154,0) 55%),
      linear-gradient(180deg, #fbf9f5 0%, #efe6d6 100%); }

  .meat-banner { position: absolute; left: 0; top: 682px; width: 1200px; height: 398px;
    background:
      radial-gradient(ellipse at 22% 55%, #7a3a20 0%, #4a1e10 35%, rgba(46,19,10,0) 60%),
      radial-gradient(ellipse at 75% 55%, #e8a866 0%, #c47038 25%, rgba(160,80,40,0) 55%),
      radial-gradient(ellipse at 85% 20%, #d89a60 0%, rgba(216,154,96,0) 40%),
      linear-gradient(90deg, var(--meat-dark) 0%, var(--meat-mid) 55%, var(--meat-light) 100%); }
  .meat-banner .banner-title { left: 165px; top: 42px; font-size: 146px; transform: rotate(-5deg); }
  .meat-banner .brand-mark { left: 455px; top: 268px; gap: 14px; }
  .meat-banner .brand-mark .dot { width: 40px; height: 40px; }
  .meat-banner .brand-mark .name { font-size: 50px; }
</style>
</head>
<body>
<main class="stall-front">

  <header class="fire-banner" role="img" aria-label="Photo of glowing charcoal grill bars with flames">
    <div class="brand-mark"><span class="dot"></span><span class="name">The Ember Coals</span></div>
    <h1 class="banner-title">The Ember Coals</h1>
  </header>

  <section class="menu-row" aria-label="Menu">
    <article class="menu-card" style="left:164px">
      <p class="card-brand">The Ember Coals</p>
      <h2 class="dish-name">Gluten Free 2<br>&amp; Vegetarian</h2>
      <div class="dish-photo photo-plate" role="img" aria-label="Plate of rice, black beans, halloumi and salad"></div>
      <span class="price">15$</span>
      <span class="new-flag">New</span>
      <p class="dish-desc roomy">Delicious Organic<br>Haloumi Cheese<br>Feijao (Organic black beans)<br>Rice and Salad</p>
    </article>

    <article class="menu-card" style="left:370px">
      <p class="card-brand">The Ember Coals</p>
      <h2 class="dish-name">BBQ Beef Feast<br>BBQ Chicken Feast</h2>
      <div class="dish-photo photo-grill" role="img" aria-label="Sliced grilled beef on the grill"></div>
      <span class="price">20$</span>
      <p class="dish-desc">Choice of beef or chicken<br>served with:<br>Feijao preto (Black bean casserole)<br>Arroz (Rice)<br>Vinaigrette Salad</p>
    </article>

    <article class="menu-card" style="left:569px">
      <p class="card-brand">The Ember Coals</p>
      <h2 class="dish-name">BBQ Beef Feast<br>BBQ Chicken Feast</h2>
      <div class="dish-photo photo-roast" role="img" aria-label="Roasted meat cuts on skewers"></div>
      <span class="price">16$</span>
      <p class="dish-desc">Choice of beef or Chicken<br>served with:<br>Feijao preto (Black bean casserole)<br>Arroz (Rice)<br>Vinaigrette Salad</p>
    </article>

    <article class="menu-card" style="left:765px">
      <p class="card-brand">The Ember Coals</p>
      <h2 class="dish-name">Gluten Free<br>&amp; Vegetarian</h2>
      <div class="dish-photo photo-veg" role="img" aria-label="Vegetarian plate with tomatoes and sauce jars"></div>
      <span class="price">18$</span>
      <p class="dish-desc roomy">Delicious Organic<br>Haloumi Cheese<br>Feijao (Organic black beans)<br>Rice and Salad</p>
    </article>

    <article class="menu-card" style="left:965px">
      <p class="card-brand">The Ember Coals</p>
      <h2 class="dish-name">BBQ Brazilian Style<br>(Picanha)</h2>
      <div class="dish-photo photo-picanha" role="img" aria-label="Picanha beef plate with tomatoes and sauce jars"></div>
      <span class="price">15$</span>
      <p class="dish-desc roomy">Award winning Angus beef, Feijao<br>(Organic black beans), Rice and salad</p>
    </article>
  </section>

  <section class="meat-banner" role="img" aria-label="Close-up photo of grilled steak and sausages">
    <h2 class="banner-title">The Ember Coals</h2>
    <div class="brand-mark"><span class="dot"></span><span class="name">The Ember Coals</span></div>
  </section>

</main>
</body>
</html>
```